Flyer für Handwerksunternehmen
Zielgruppe
Wir sind ein Handwerksunternehmen. Wir bieten alle Leistungen aus einer Hand. Mehr Infos unter www.werkbaukolleg.de
Aufgabenstellung
Modernes Design

```html
<!DOCTYPE html>
<html lang="de">
<head>
<meta charset="utf-8">
<title>Werkbaukolleg – Flyer</title>
<link href="https://fonts.googleapis.com/css2?family=Poppins:wght@400;500;600;700&family=Oswald:wght@300;400&display=swap" rel="stylesheet">
<style>
  :root{
    --stage:#1d1d1d;
    --paper:#ffffff;
    --paper-grey:#ececec;
    --green-dark:#1e6b35;
    --green-deep:#1d5a2c;
    --green-light:#5c9b3c;
    --green-lime:#8db446;
    --text-grey:#555555;
    --white:#ffffff;
  }
  *{box-sizing:border-box;margin:0;padding:0}
  html,body{width:1200px;height:808px;overflow:hidden;background:var(--stage)}
  .canvas{position:relative;width:1200px;height:808px;background:var(--stage);font-family:"Poppins",sans-serif}
  .page{position:absolute;top:124px;width:560px;height:560px;overflow:hidden}
  .page--front{left:39px;background:var(--paper)}
  .page--back{left:622px;background:var(--paper-grey)}
  .abs{position:absolute}

  /* brand name */
  .brand{display:flex;align-items:center;gap:6px;color:var(--green-deep);font-weight:700;font-size:13px;letter-spacing:.5px}
  .brand__dot{width:10px;height:10px;background:var(--green-light)}

  /* front */
  .headline{left:20px;top:178px;color:var(--green-deep);font-weight:700;font-size:22.5px;line-height:26px;letter-spacing:.3px}
  .intro{left:19px;top:280px;width:311px;height:250px;background:var(--green-light);
    clip-path:polygon(0 0,88% 0,100% 13%,100% 100%,12% 100%,0 88%);
    padding:20px 21px 0 21px;color:var(--white);font-size:12px;line-height:14.8px;text-align:justify}
  .skills-title{left:380px;top:302px;width:130px;text-align:center;color:var(--green-deep);line-height:20px}
  .skills-title span{display:block}
  .skills-title .light{font-weight:400;font-size:16px;color:#333}
  .skills-title .bold{font-weight:700;font-size:16.5px;color:var(--green-light)}
  .tile{width:60px;height:80px;display:flex;flex-direction:column;align-items:center;padding-top:10px;
    font-family:"Oswald",sans-serif;font-weight:300;font-size:7.5px;line-height:11px;text-align:center;
    clip-path:polygon(0 0,88% 0,100% 10%,100% 100%,12% 100%,0 90%)}
  .tile svg{width:28px;height:24px;margin-bottom:10px}
  .tile--outline{border:1px solid var(--green-deep);background:var(--paper);color:var(--green-light)}
  .tile--dark{background:var(--green-deep);color:var(--white)}
  .tile--light{background:var(--green-light);color:var(--white)}

  /* back */
  .section-title{left:21px;top:24px;color:var(--white);font-weight:700;font-size:22px;letter-spacing:.5px}
  .service{width:154px}
  .service__photo{height:110px}
  .service__label{height:31px;background:var(--green-dark);color:var(--white);font-weight:500;font-size:13.5px;
    display:flex;align-items:center;justify-content:center;text-align:center;line-height:13px;
    clip-path:polygon(0 0,100% 0,100% 100%,9% 100%,0 70%)}
  .service__label--small{font-size:11px}
  .question{left:23px;top:242px;width:170px;font-family:"Oswald",sans-serif;font-weight:400;font-size:18px;line-height:23.6px;color:var(--green-deep)}
  .contact{left:19px;top:423px;width:518px;height:120px;background:var(--white);
    clip-path:polygon(0 0,97% 0,100% 10%,100% 100%,0 100%)}
  .contact__brand{left:22px;top:52px}
  .contact__address{left:164px;top:26px;color:var(--text-grey);font-size:14px;line-height:18px}
  .contact__phone{left:330px;top:21px;color:var(--green-deep);font-weight:700;font-size:21px;letter-spacing:.3px}
  .contact__mail{left:163px;top:69px;color:var(--text-grey);font-size:14.5px;line-height:21px}
  .phone-badge{left:262px;top:405px;width:38px;height:38px}
</style>
</head>
<body>
<div class="canvas">

  <!-- Vorderseite -->
  <section class="page page--front">
    <svg class="abs" width="560" height="560" viewBox="0 0 560 560" style="left:0;top:0">
      <polygon points="0,177 219,69 219,76 0,187" fill="var(--green-lime)"/>
      <defs>
        <linearGradient id="buildingTone" x1="0" y1="0" x2="1" y2="1">
          <stop offset="0" stop-color="#d8d8d4"/>
          <stop offset=".5" stop-color="#7c9a5a"/>
          <stop offset="1" stop-color="#4e5a4a"/>
        </linearGradient>
      </defs>
      <polygon role="img" aria-label="Foto eines begrünten Wohnhochhauses mit Dachterrassen"
        points="300,14 430,40 510,110 520,300 440,300 380,290 300,230 220,130"
        fill="url(#buildingTone)"/>
      <polygon points="390,300 560,196 560,220 400,310" fill="var(--green-deep)"/>
    </svg>

    <div class="abs brand" style="left:20px;top:80px">
      <span class="brand__dot"></span>WERKBAUKOLLEG
    </div>

    <h1 class="abs headline">BAUMANAGEMENT<br>MIT LANGJÄHRIGER<br>ERFAHRUNG</h1>

    <p class="abs intro">WERKBAUKOLLEG unterstützen Sie bei Ihrem Bauprojekt mit einer umfassenden Baubetreuung und Ausführung. Schon in der frühen Planungsphase stimmen wir die Ziele gemeinsam mit unseren Auftraggebern ab und leiten ein effizientes wie transparentes Baumanagement in die Wege. In vielen Phasen unterstützen wir Sie direkt mit unseren geschulten eigenen Mitarbeitern oder verschiedenen Partnerfirmen aus unserem Netzwerk. Von der Ausschreibung bis hin zur Dokumentation begleiten wir Ihr Projekt und stellen sicher, dass Ihre Ziele erreicht werden.</p>

    <h2 class="abs skills-title"><span class="light">UNSERE</span><span class="bold">KOMPETENZEN</span></h2>

    <div class="abs tile tile--outline" style="left:341px;top:356px">
      <svg viewBox="0 0 28 24" fill="none" stroke="currentColor" stroke-width="1.2"><rect x="2" y="3" width="20" height="16"/><path d="M6 3v16M10 7h8M10 11h8M10 15h5"/><path d="M19 20a4 4 0 0 1 8 0z"/></svg>
      <span>Umfassende<br>Baubetreuung</span>
    </div>
    <div class="abs tile tile--dark" style="left:412px;top:356px">
      <svg viewBox="0 0 28 24" fill="none" stroke="currentColor" stroke-width="1.2"><rect x="2" y="3" width="20" height="16"/><path d="M6 3v16M10 7h8M10 11h8M10 15h5"/><path d="M19 20a4 4 0 0 1 8 0z"/></svg>
      <span>Deutschlandweit<br>Tätig</span>
    </div>
    <div class="abs tile tile--outline" style="left:482px;top:356px">
      <svg viewBox="0 0 28 24" fill="none" stroke="currentColor" stroke-width="1.2"><rect x="2" y="3" width="20" height="16"/><path d="M6 3v16M10 7h8M10 11h8M10 15h5"/><path d="M19 20a4 4 0 0 1 8 0z"/></svg>
      <span>Langjährige<br>Erfahrung</span>
    </div>
    <div class="abs tile tile--light" style="left:341px;top:450px">
      <svg viewBox="0 0 28 24" fill="none" stroke="currentColor" stroke-width="1.2"><rect x="2" y="3" width="20" height="16"/><path d="M6 3v16M10 7h8M10 11h8M10 15h5"/><path d="M19 20a4 4 0 0 1 8 0z"/></svg>
      <span>Mitarbeiter Aus Allen<br>Handwerksbereichen</span>
    </div>
    <div class="abs tile tile--outline" style="left:412px;top:450px">
      <svg viewBox="0 0 28 24" fill="none" stroke="currentColor" stroke-width="1.2"><rect x="2" y="3" width="20" height="16"/><path d="M6 3v16M10 7h8M10 11h8M10 15h5"/><path d="M19 20a4 4 0 0 1 8 0z"/></svg>
      <span>Umfangreiches<br>Partnernetzwerk</span>
    </div>
    <div class="abs tile tile--light" style="left:482px;top:450px">
      <svg viewBox="0 0 28 24" fill="none" stroke="currentColor" stroke-width="1.2"><rect x="2" y="3" width="20" height="16"/><path d="M6 3v16M10 7h8M10 11h8M10 15h5"/><path d="M19 20a4 4 0 0 1 8 0z"/></svg>
      <span>Alle Leistungen<br>Aus Einer Hand</span>
    </div>
  </section>

  <!-- Rückseite -->
  <section class="page page--back">
    <svg class="abs" width="560" height="560" viewBox="0 0 560 560" style="left:0;top:0">
      <polygon points="0,0 255,0 0,123" fill="var(--green-light)"/>
    </svg>
    <h2 class="abs section-title">LEISTUNGEN</h2>

    <div class="abs service" style="left:24px;top:80px">
      <div class="service__photo" role="img" aria-label="Foto: Hände zeigen auf Baupläne am Schreibtisch" style="background:linear-gradient(135deg,#e9e6e0,#bdb8ae)"></div>
      <div class="service__label">AUSSCHREIBUNG</div>
    </div>
    <div class="abs service" style="left:198px;top:80px">
      <div class="service__photo" role="img" aria-label="Foto: Handschlag über Bauplänen und Schutzhelm" style="background:linear-gradient(135deg,#cfd2d4,#8d9296)"></div>
      <div class="service__label">VERGABE</div>
    </div>
    <div class="abs service" style="left:372px;top:80px">
      <div class="service__photo" role="img" aria-label="Foto: Laptop und Bauhelm auf einer Baustelle" style="background:linear-gradient(180deg,#9fb7c4,#6f8f5a 45%,#c9c9c6)"></div>
      <div class="service__label service__label--small">OBJEKTÜBERWACHUNG</div>
    </div>
    <div class="abs service" style="left:198px;top:238px">
      <div class="service__photo" role="img" aria-label="Foto: moderne Wohnanlage mit begrünten Terrassen" style="background:linear-gradient(180deg,#a9bccb,#7a5a45 50%,#5b7a3c)"></div>
      <div class="service__label">OBJEKTBETREUUNG<br>DOKUMENTATION</div>
    </div>
    <div class="abs service" style="left:372px;top:238px">
      <div class="service__photo" role="img" aria-label="Foto: Holz- und Materialmuster in der Hand" style="background:linear-gradient(135deg,#8a5a3a,#c9a176 55%,#e6e2dc)"></div>
      <div class="service__label">BAUMATERIALIEN<br>BEMUSTERN</div>
    </div>

    <p class="abs question">Benötigen Sie Für Ihr Projekt Eine Erstklassige Dienstleistung, Die Ihren Ansprüchen Gerecht Wird Und Dennoch Preiswert Ist?</p>

    <div class="abs contact">
      <div class="abs brand contact__brand"><span class="brand__dot"></span>WERKBAUKOLLEG</div>
      <p class="abs contact__address">Am Talgraben 12<br>Wiesloch 69168</p>
      <p class="abs contact__phone">06221-4730150</p>
      <p class="abs contact__mail">kontakt@werkbaukolleg.deWiesloch<br>www.werkbaukolleg.deWiesloch</p>
    </div>

    <svg class="abs phone-badge" viewBox="0 0 38 38">
      <circle cx="19" cy="19" r="18" fill="var(--white)" stroke="var(--green-dark)" stroke-width="2.5"/>
      <path d="M13 10c1-1 2.5-1 3 0l1.8 3.5c.4.8.2 1.6-.5 2.1l-1.3 1c.9 2.2 2.6 4 4.8 5l1-1.3c.5-.7 1.4-.9 2.1-.5l3.5 1.8c1 .5 1 2 0 3l-1.5 1.5c-1.3 1.3-3.3 1.5-5 .6-4.2-2.2-7.5-5.6-9.6-9.8-.9-1.7-.6-3.7.7-5z" fill="none" stroke="var(--green-dark)" stroke-width="1.8"/>
    </svg>
  </section>

</div>
</body>
</html>
```